Core Values Poster for Healthcare company

Trying to Create a core values poster for my company. Healthcare Company - We have Neurosurgery, Pain Management, Physical Therapy, Occupational Therapy, Rehab, Imaging, and psychology so far and we are growing fast.

Core Values would Include - (Execution), (Loyalty), (Innovation), (Synergy), (Growth-Oriented), (Ethics & Integrity), (Love), and (Energy)

Please incorporate the Company Logo which is on the website and I have included it in my uploads. As long as the logo stays blue it does not need a gradient effect.

I like the posters made for this contest : https://quillvane.com.au/poster-design/contests/make-team-principles-wallchart-815327

This picture should be memorable so people know our Core Values

Target Market(s)

Staff in the company

Colors

Designer to choose colors to be used in the design.

Requirements
Must have
• Logo
Nice to have
• Pictures for each core value

```html
<!DOCTYPE html>
<html lang="en">
<head>
<meta charset="utf-8">
<title>Kestreline Core Values Poster</title>
<link rel="stylesheet" href="https://fonts.googleapis.com/css2?family=Cinzel:wght@500;700&family=Open+Sans:wght@800&display=swap">
<style>
  :root {
    --page-bg: #e9ebec;
    --paper: #ffffff;
    --brand-blue: #1f8fc4;
    --brand-deep: #1b7fb3;
    --tile-top: #ffffff;
    --tile-bottom: #dfe6ec;
    --mist: #bfe3f3;
    --ribbon: #d3ebf5;
    --ribbon-fold: #a9cde0;
  }
  html, body {
    margin: 0;
    width: 1200px;
    height: 1200px;
    overflow: hidden;
    background: var(--page-bg);
  }
  .poster {
    position: absolute;
    left: 213px;
    top: 30px;
    width: 774px;
    height: 1140px;
    background: var(--paper);
    box-shadow: 0 4px 14px rgba(0,0,0,.18);
    overflow: hidden;
  }
  .poster__frame {
    position: absolute;
    inset: 19px;
    border: 2px solid var(--brand-blue);
  }
  .network {
    position: absolute;
    border-radius: 50%;
    filter: blur(2px);
  }
  .network--top {
    left: 0; top: 20px; width: 774px; height: 260px;
    background:
      radial-gradient(ellipse at 15% 55%, rgba(31,143,196,.35), transparent 45%),
      radial-gradient(ellipse at 85% 50%, rgba(31,143,196,.4), transparent 45%),
      radial-gradient(ellipse at 50% 85%, rgba(31,143,196,.3), transparent 50%),
      radial-gradient(ellipse at 50% 50%, var(--mist), transparent 70%);
    opacity: .7;
  }
  .network--bottom {
    left: 40px; top: 880px; width: 700px; height: 260px;
    background:
      radial-gradient(ellipse at 30% 50%, rgba(31,143,196,.25), transparent 55%),
      radial-gradient(ellipse at 70% 40%, rgba(31,143,196,.25), transparent 55%);
    opacity: .8;
  }
  .brand {
    position: absolute;
    left: 0; right: 0; top: 34px;
    display: flex;
    justify-content: center;
    align-items: center;
    gap: 12px;
    color: var(--brand-blue);
    font-family: 'Cinzel', serif;
    font-weight: 500;
    font-size: 46px;
    letter-spacing: 2px;
  }
  .brand__mark {
    width: 44px; height: 44px;
    background: var(--brand-blue);
  }
  .ribbon {
    position: absolute;
    left: 138px; top: 150px;
    width: 499px; height: 76px;
  }
  .ribbon__title {
    position: absolute;
    left: 0; right: 0; top: 14px;
    text-align: center;
    font-family: 'Cinzel', serif;
    font-weight: 700;
    font-size: 44px;
    color: var(--brand-blue);
  }
  .connectors {
    position: absolute;
    left: 0; top: 0;
  }
  .value-tile {
    position: absolute;
    width: 207px;
    height: 242px;
    box-sizing: border-box;
    border: 4px solid var(--brand-blue);
    border-radius: 34px;
    background: radial-gradient(ellipse at 50% 35%, var(--tile-top), var(--tile-bottom));
    box-shadow: 0 3px 8px rgba(0,0,0,.22);
  }
  .value-tile--center { width: 211px; height: 226px; }
  .value-tile__icon {
    position: absolute;
    left: 50%;
    top: 30px;
    transform: translateX(-50%);
    width: 140px;
    height: 130px;
  }
  .value-tile__figure {
    position: absolute;
    left: 50%;
    top: 36px;
    transform: translateX(-50%);
    width: 130px;
    height: 120px;
    border-radius: 18px;
    background: radial-gradient(circle at 50% 45%, var(--brand-blue), rgba(31,143,196,.35));
  }
  .value-tile__label {
    position: absolute;
    left: 0; right: 0; bottom: 30px;
    text-align: center;
    font-family: 'Open Sans', sans-serif;
    font-weight: 800;
    font-size: 15px;
    line-height: 19px;
    letter-spacing: .3px;
    color: var(--brand-deep);
  }
</style>
</head>
<body>
<main class="poster">
  <div class="network network--top" role="img" aria-label="Soft blue molecular network pattern"></div>
  <div class="network network--bottom" role="img" aria-label="Soft blue molecular network pattern"></div>
  <div class="poster__frame"></div>

  <header class="brand">
    <span class="brand__mark"></span>
    <span class="brand__name">KESTRELINE</span>
  </header>

  <div class="ribbon">
    <svg width="499" height="76" viewBox="0 0 499 76">
      <polygon points="0,14 50,10 50,66 20,66 36,40" fill="var(--ribbon-fold)"/>
      <polygon points="499,14 449,10 449,66 479,66 463,40" fill="var(--ribbon-fold)"/>
      <rect x="42" y="2" width="415" height="64" fill="var(--ribbon)"/>
    </svg>
    <div class="ribbon__title">CORE VALUES</div>
  </div>

  <svg class="connectors" width="774" height="1140" viewBox="0 0 774 1140" fill="none" stroke="var(--brand-blue)" stroke-width="4">
    <line x1="389" y1="376" x2="389" y2="946"/>
    <path d="M255 376 H520 M255 659 H520 M255 946 H520"/>
    <g fill="var(--brand-blue)" stroke="none">
      <circle cx="389" cy="376" r="10"/>
      <circle cx="389" cy="659" r="10"/>
      <circle cx="389" cy="946" r="10"/>
    </g>
  </svg>

  <section class="value-tile" style="left:52px; top:290px;">
    <svg class="value-tile__icon" viewBox="0 0 140 130" fill="var(--brand-blue)">
      <g transform="translate(56 74)">
        <rect x="-9" y="-54" width="18" height="108" rx="3"/>
        <rect x="-9" y="-54" width="18" height="108" rx="3" transform="rotate(45)"/>
        <rect x="-9" y="-54" width="18" height="108" rx="3" transform="rotate(90)"/>
        <rect x="-9" y="-54" width="18" height="108" rx="3" transform="rotate(135)"/>
        <circle r="40"/>
        <circle r="15" fill="#fff"/>
      </g>
      <g transform="translate(110 28)">
        <rect x="-5" y="-26" width="10" height="52" rx="2"/>
        <rect x="-5" y="-26" width="10" height="52" rx="2" transform="rotate(45)"/>
        <rect x="-5" y="-26" width="10" height="52" rx="2" transform="rotate(90)"/>
        <rect x="-5" y="-26" width="10" height="52" rx="2" transform="rotate(135)"/>
        <circle r="19"/>
        <circle r="7" fill="#fff"/>
      </g>
    </svg>
    <div class="value-tile__label">EXECUTION</div>
  </section>

  <section class="value-tile" style="left:516px; top:290px;">
    <div class="value-tile__figure" role="img" aria-label="Handshake illustration"></div>
    <div class="value-tile__label">LOYALTY</div>
  </section>

  <section class="value-tile value-tile--center" style="left:283px; top:403px;">
    <div class="value-tile__figure" role="img" aria-label="Head with lightbulb illustration"></div>
    <div class="value-tile__label">INNOVATION</div>
  </section>

  <section class="value-tile" style="left:52px; top:572px;">
    <div class="value-tile__figure" role="img" aria-label="Two people illustration"></div>
    <div class="value-tile__label">SYNERGY</div>
  </section>

  <section class="value-tile" style="left:516px; top:572px;">
    <svg class="value-tile__icon" viewBox="0 0 140 130" fill="var(--brand-blue)">
      <rect x="16" y="78" width="22" height="50"/>
      <rect x="50" y="88" width="22" height="40"/>
      <rect x="84" y="60" width="22" height="68"/>
      <polyline points="10,80 40,52 66,76 114,24" fill="none" stroke="var(--brand-blue)" stroke-width="9"/>
      <polygon points="100,14 128,8 122,36"/>
    </svg>
    <div class="value-tile__label">GROWTH-ORIENTED</div>
  </section>

  <section class="value-tile value-tile--center" style="left:283px; top:688px;">
    <svg class="value-tile__icon" viewBox="0 0 140 130" fill="none" stroke="var(--brand-blue)" stroke-width="4">
      <path d="M70 110 L24 64 C8 48 14 22 36 20 C52 19 62 28 70 40 C78 28 88 19 104 20 C126 22 132 48 116 64 Z"/>
    </svg>
    <div class="value-tile__label">LOVE</div>
  </section>

  <section class="value-tile" style="left:52px; top:855px;">
    <div class="value-tile__figure" role="img" aria-label="Shield illustration for ethics and integrity"></div>
    <div class="value-tile__label">ETHICS &amp;<br>INTEGRITY</div>
  </section>

  <section class="value-tile" style="left:516px; top:855px;">
    <div class="value-tile__figure" role="img" aria-label="Lightning bolt illustration for energy"></div>
    <div class="value-tile__label">ENERGY</div>
  </section>
</main>
</body>
</html>
```